Bindle Rust Mustard - Australian Iconic Label

Label design. This first label will be part of a growing set of Australian Condiments. We would like the label to be iconic of Australia. We would like to sell this product as an Australian souvenir at airports, Australiana gift stores, tourism destinations etc. We would like an Australian iconic image to sit in the background on the centre diamond. We would prefer it was not limited to regional icons more generic icons for example kangaroo and emu so it doesn't matter which state or destination it is sold. This range can look different to our other range of products as they will not necessarily sell at the same places but we would still like customers to identify that they are Pembroke's Morsels. I've included some other labels we use on this jar so you can replicate colours and size of the label (details on files + width of band 35mm).
P.s. it requires a sealing tab integrated into the design.
Brand name: Pembroke's Morsels
Produced at The Crumb Works
www.crumbworks.com.au
IF you would like any further direction please don't hesitate to ask.

Target Market(s)

Tourism
Souvenir
Gift

```html
<!DOCTYPE html>
<html lang="en">
<head>
<meta charset="utf-8">
<title>Bindle Rust Mustard – Label</title>
<link rel="stylesheet" href="https://fonts.googleapis.com/css2?family=Alfa+Slab+One&family=Lato:wght@700;900&display=swap">
<style>
  :root {
    --backdrop: #e4e4e4;
    --maroon: #8c1d4a;
    --green: #1f7a4a;
    --cream: #f3ead0;
    --gold: #f3b21c;
    --ink: #2a1a0c;
    --emblem-dark: #2b2217;
  }
  * { box-sizing: border-box; margin: 0; padding: 0; }
  html, body { width: 1200px; height: 856px; overflow: hidden; }
  body { background: var(--backdrop); position: relative; font-family: "Lato", sans-serif; }

  .seal-tab { position: absolute; left: 568px; top: 14px; width: 64px; height: 70px; }

  .label {
    position: absolute; left: 80px; top: 260px;
    width: 1040px; height: 552px;
    background: var(--cream);
  }
  .band { position: absolute; left: 0; width: 100%; background: var(--maroon); }
  .band--top { top: 0; height: 78px; border-bottom: 10px solid var(--green); }
  .band--bottom {
    bottom: 0; height: 80px;
    border-top: 10px solid var(--green); border-bottom: 6px solid var(--green);
    display: flex; align-items: center; justify-content: center;
  }
  .tagline { color: var(--gold); font-weight: 700; font-size: 19px; letter-spacing: 0.3px; }

  .product-name {
    position: absolute; left: 0; right: 0; top: 264px;
    text-align: center;
    font-family: "Alfa Slab One", serif;
    font-size: 72px; line-height: 1;
    color: var(--gold);
    -webkit-text-stroke: 3px var(--ink);
    text-shadow: 3px 4px 0 var(--ink);
    letter-spacing: 1px;
    white-space: nowrap;
  }
  .net-weight {
    position: absolute; right: 12px; top: 420px;
    font-family: "Alfa Slab One", serif; font-size: 20px; color: var(--ink);
  }

  .emblem { position: absolute; left: 392px; top: 62px; width: 416px; height: 373px; }

  .brand-plate {
    position: absolute; left: 414px; top: 312px;
    width: 372px; height: 100px;
    background: var(--cream);
    border: 5px solid var(--emblem-dark);
    display: flex; flex-direction: column; align-items: center; justify-content: center;
  }
  .brand-name {
    font-family: "Alfa Slab One", serif; font-size: 30px; line-height: 1.1;
    color: var(--emblem-dark); letter-spacing: 6px;
    text-align: center;
  }
</style>
</head>
<body>
  <svg class="seal-tab" viewBox="0 0 64 70" role="img" aria-label="Sealing tab folding over the lid">
    <path d="M4 70 V16 Q4 2 18 2 H46 Q60 2 60 16 V70 Z" fill="var(--maroon)" stroke="var(--green)" stroke-width="4"/>
    <line x1="6" y1="40" x2="58" y2="40" stroke="var(--gold)" stroke-width="2" stroke-dasharray="5 4"/>
  </svg>

  <section class="label">
    <div class="band band--top"></div>
    <h1 class="product-name">BINDLE RUST MUSTARD</h1>
    <p class="net-weight">200gms</p>
    <div class="band band--bottom">
      <p class="tagline">Proudly Australian owned and made</p>
    </div>
  </section>

  <svg class="emblem" viewBox="0 0 416 373" role="img" aria-label="Australian outback scene illustration in the centre diamond">
    <defs>
      <linearGradient id="emblemFill" x1="0" y1="0" x2="0" y2="1">
        <stop offset="0" stop-color="#e0b75a"/>
        <stop offset="0.55" stop-color="#c99a3a"/>
        <stop offset="1" stop-color="#2b2217"/>
      </linearGradient>
    </defs>
    <polygon points="208,2 414,186.5 208,371 2,186.5" fill="var(--green)"/>
    <polygon points="208,18 396,186.5 208,355 20,186.5" fill="var(--cream)"/>
    <polygon points="208,28 385,186.5 208,345 31,186.5" fill="url(#emblemFill)"/>
  </svg>

  <div class="brand-plate">
    <span class="brand-name">PEMBROKE'S</span>
    <span class="brand-name">MORSELS</span>
  </div>
</body>
</html>
```